Business Cards for Internet Security Company

Awesome designers! This is the opportunity to help design cards for a forward thinking network security company. They use threat information gathered from peer groups to make intelligent decisions on what threats are relevant and which arent. ( not that you need this to do designs, but just so you know where they are coming from. ) :-)

We'd like to see a two side design and the deliverables will be in illustrator 4. The logo is attached and the logo colors are attached in the JPG and I've attached a an eps of the logo and icon

```html
<!DOCTYPE html>
<html lang="en">
<head>
<meta charset="utf-8">
<title>Norvale Business Cards</title>
<link href="https://fonts.googleapis.com/css2?family=Questrial&family=Roboto+Condensed:wght@300;700&display=swap" rel="stylesheet">
<style>
  :root {
    --page-bg: #e9e6e1;
    --card-light: #7aaee0;
    --card-mid: #3d6fa6;
    --card-dark: #132947;
    --ink-white: #ffffff;
    --ink-soft: #dce8f5;
    --accent-blue: #6fb0ee;
    --edge: #0e1f38;
  }
  * { margin: 0; padding: 0; box-sizing: border-box; }
  html, body {
    width: 1200px; height: 1000px; overflow: hidden;
    background: var(--page-bg);
  }
  .sheet {
    position: relative; width: 1200px; height: 1000px;
    display: flex; flex-direction: column; align-items: center; justify-content: center;
    gap: 60px;
  }
  .card {
    position: relative; width: 700px; height: 400px; border-radius: 26px; overflow: hidden;
    background:
      radial-gradient(ellipse 60% 90% at 8% 95%, rgba(150,200,245,.55), transparent 70%),
      linear-gradient(35deg, var(--card-light) 0%, var(--card-mid) 38%, var(--card-dark) 78%);
    box-shadow: 0 6px 0 var(--edge), 0 14px 28px rgba(0,0,0,.28);
  }
  .card .sheen {
    position: absolute; inset: 0;
    background: linear-gradient(172deg, transparent 55%, rgba(255,255,255,.08) 62%, transparent 70%);
  }
  /* Front */
  .front-brand {
    position: absolute; left: 0; right: 0; top: 0; bottom: 0;
    display: flex; align-items: center; justify-content: center; gap: 22px;
  }
  .brand-dot {
    width: 72px; height: 72px; border-radius: 50%; border: 11px solid var(--ink-white);
  }
  .brand-name {
    font-family: "Questrial", sans-serif; font-size: 110px; color: var(--ink-white);
    letter-spacing: 1px; line-height: 1;
  }
  /* Back */
  .back-mark {
    position: absolute; left: 70px; top: 110px; width: 200px; height: 200px;
    border-radius: 50%; border: 30px solid var(--ink-white);
  }
  .back-info {
    position: absolute; left: 360px; top: 70px; padding-left: 28px;
    border-left: 2px solid rgba(255,255,255,.75);
    font-family: "Roboto Condensed", sans-serif; color: var(--ink-soft);
  }
  .person-first { font-weight: 300; font-size: 44px; color: var(--ink-white); line-height: 1; letter-spacing: 1px; }
  .person-last { font-weight: 700; font-size: 30px; color: var(--accent-blue); line-height: 1.1; letter-spacing: 1px; }
  .person-title { font-weight: 300; font-size: 17px; margin-bottom: 22px; }
  .contact { list-style: none; font-weight: 300; font-size: 16px; line-height: 1.35; }
  .contact li { display: flex; gap: 10px; align-items: flex-start; margin-bottom: 10px; }
  .contact svg { width: 14px; height: 14px; flex: none; margin-top: 3px; fill: var(--ink-white); }
</style>
</head>
<body>
<main class="sheet">
  <section class="card card-front" aria-label="Card front">
    <div class="sheen"></div>
    <div class="front-brand">
      <span class="brand-dot"></span>
      <span class="brand-name">Norvale</span>
    </div>
  </section>

  <section class="card card-back" aria-label="Card back">
    <div class="sheen"></div>
    <span class="back-mark"></span>
    <div class="back-info">
      <p class="person-first">ALEX</p>
      <p class="person-last">MARLOW</p>
      <p class="person-title">Vice President</p>
      <ul class="contact">
        <li>
          <svg viewBox="0 0 14 14"><path d="M7 0a5 5 0 0 0-5 5c0 4 5 9 5 9s5-5 5-9a5 5 0 0 0-5-5zm0 7a2 2 0 1 1 0-4 2 2 0 0 1 0 4z"/></svg>
          <span>P.O. Box 2210, 00200<br>GPO Riverton, Elmshire</span>
        </li>
        <li>
          <svg viewBox="0 0 14 14"><path d="M3 1l2 3-1.5 1.5a8 8 0 0 0 5 5L10 9l3 2-1 2.5C6 13 1 8 .5 2z"/></svg>
          <span>+41 555 01 42<br>+41 555 01 87</span>
        </li>
        <li>
          <svg viewBox="0 0 14 14"><path d="M1 3h12v8H1zm1 1v.5l5 3.5 5-3.5V4z"/></svg>
          <span>alex@norvale.com</span>
        </li>
        <li>
          <svg viewBox="0 0 14 14"><circle cx="7" cy="7" r="6" fill="none" stroke="#fff" stroke-width="1.3"/><path d="M1 7h12M7 1c-3 3-3 9 0 12M7 1c3 3 3 9 0 12" fill="none" stroke="#fff" stroke-width="1.1"/></svg>
          <span>www.norvale.com</span>
        </li>
      </ul>
    </div>
  </section>
</main>
</body>
</html>
```